Catchy Cards for Hospital

I run a rural hospital in Texas called Pellor Valley Hospital and am in need of contemporary business cards for all of my Department Heads. While our logo is somewhat simplistic, I don't have the option of changing it at this time, so anything to make the rest of the card present the appearance of a modern, professional healthcare facility would be great. Although the attached files are in black, our hospital colors are in a copper brown and black. I need to be able to change the name and title on the card so I can get cards printed for various department heads.

Target Market(s)

Referring physicians, large hospital systems, national organizations, state and federal government

Industry/Entity Type

Hospital

Contact Information for Business Card

Name Dale Hoskin
Title CEO

Phone: Main 555-555-0147 & Direct xxxxxx
Fax xxxxx
dale.hoskin@pellorvh.example
382 Wimble Street Box 415
Halvern, Tenoria 76902

Font styles to use
Serif

Colors
f48340

Requirements
Must have
• Clean crisp lines and ability to modify names, titles and emails
• On the back "PellorValleyHospital.Example
Nice to have
• Needs to be in line with logo, which is a bit dated and not too appealing, but I'm hoping that the rest of the card can make up for that fact just a little bit.
• Hospital's colors are a copper brown, black and white
Should not have
• Shapes or anything distracting

```html
<!DOCTYPE html>
<html lang="en">
<head>
<meta charset="utf-8">
<title>Pellor Valley Hospital – Business Card</title>
<link href="https://fonts.googleapis.com/css2?family=Roboto+Condensed:wght@400;700&display=swap" rel="stylesheet">
<style>
  :root {
    --backdrop: #4a3f37;
    --ink: #0b0b0b;
    --paper: #f4f4f2;
    --panel: #000000;
    --edge-grey: #b9b9b9;
    --light-text: #ffffff;
  }
  * { box-sizing: border-box; margin: 0; padding: 0; }
  html, body {
    width: 1200px; height: 886px; overflow: hidden;
    background: var(--backdrop);
    font-family: "Roboto Condensed", Arial, sans-serif;
  }
  .stage { position: relative; width: 1200px; height: 886px; }

  .card {
    position: absolute; width: 540px; height: 309px;
    box-shadow: 0 14px 30px rgba(0,0,0,.45);
    overflow: hidden;
  }

  /* Back of card */
  .card-back { left: 70px; top: 130px; background: var(--panel); color: var(--light-text); }
  .card-back .wordmark {
    position: absolute; left: 0; right: 0; top: 76px;
    text-align: center; font-size: 38px; line-height: 1.05; font-weight: 400;
  }
  .card-back .web {
    position: absolute; left: 0; right: 0; bottom: 46px;
    text-align: center; font-size: 14px; font-weight: 700; letter-spacing: .2px;
  }

  /* Front of card */
  .card-front { left: 600px; top: 440px; background: var(--paper); color: var(--ink); }
  .card-front .swoosh { position: absolute; inset: 0; }
  .card-front .wordmark {
    position: absolute; left: 44px; top: 96px;
    font-size: 38px; line-height: 1.05; font-weight: 400; color: var(--ink);
  }
  .contact {
    position: absolute; right: 24px; top: 58px; width: 210px;
    text-align: right; color: var(--light-text);
  }
  .contact .name { font-size: 17px; font-weight: 700; letter-spacing: .4px; }
  .contact .title { font-size: 12px; margin-bottom: 16px; }
  .contact .line { font-size: 12.5px; line-height: 17px; }
  .contact .gap { height: 12px; }
  .contact .row { display: flex; justify-content: flex-end; align-items: center; gap: 6px; font-size: 12.5px; line-height: 17px; white-space: nowrap; }
  .icon { width: 12px; height: 12px; flex: none; }
</style>
</head>
<body>
<main class="stage">

  <section class="card card-back" aria-label="Card back">
    <p class="wordmark">Pellor<br>Valley<br>Hospital</p>
    <p class="web">www.PellorValleyHospital.Example</p>
  </section>

  <section class="card card-front" aria-label="Card front">
    <svg class="swoosh" viewBox="0 0 540 309" preserveAspectRatio="none" aria-hidden="true">
      <path d="M352 0 C300 40 300 120 300 180 C300 250 280 290 250 309 L540 309 L540 0 Z" fill="var(--edge-grey)"/>
      <path d="M366 0 C318 40 314 120 314 180 C314 250 300 290 272 309 L540 309 L540 0 Z" fill="var(--panel)"/>
    </svg>

    <p class="wordmark">Pellor<br>Valley<br>Hospital</p>

    <div class="contact">
      <p class="name">DALE HOSKIN</p>
      <p class="title">CEO</p>
      <p class="line">382 Wimble Street Box 415</p>
      <p class="line">Halvern, Tenoria 76902</p>
      <div class="gap"></div>
      <p class="row">555-555-0147
        <svg class="icon" viewBox="0 0 24 24" aria-hidden="true"><path fill="#fff" d="M6.6 10.8a15 15 0 0 0 6.6 6.6l2.2-2.2c.3-.3.7-.4 1-.2 1.1.4 2.3.6 3.6.6.6 0 1 .4 1 1V20c0 .6-.4 1-1 1A17 17 0 0 1 3 4c0-.6.4-1 1-1h3.5c.6 0 1 .4 1 1 0 1.3.2 2.5.6 3.6.1.3 0 .7-.2 1z"/></svg>
      </p>
      <p class="row">555-555-0183
        <svg class="icon" viewBox="0 0 24 24" aria-hidden="true"><path fill="#fff" d="M7 3h8l3 3v4H7zM4 11h16a1 1 0 0 1 1 1v7a1 1 0 0 1-1 1H4a1 1 0 0 1-1-1v-7a1 1 0 0 1 1-1z"/></svg>
      </p>
      <div class="gap"></div>
      <p class="row">dale.hoskin@pellorvh.example
        <svg class="icon" viewBox="0 0 24 24" aria-hidden="true"><path fill="#fff" d="M3 5h18v14H3z"/><path d="M3 5l9 7 9-7" fill="none" stroke="#000" stroke-width="2"/></svg>
      </p>
      <p class="row">PellorValleyHospital.Example
        <svg class="icon" viewBox="0 0 24 24" aria-hidden="true"><circle cx="12" cy="12" r="10" fill="#fff"/><path d="M2 12h20M12 2c3 3 3 17 0 20M12 2c-3 3-3 17 0 20" fill="none" stroke="#000" stroke-width="1.5"/></svg>
      </p>
    </div>
  </section>

</main>
</body>
</html>
```